design a construction company business card

Design business card around our logo. Card must have all the typical info: name, title, address, phone, email, business name, etc. Somewhere on the card I would like to see our motto "Built on trust... Driven by craftsmanship." Consider adding a splash of bright orange to the card to complement the blues and silvers/grays in the logo. We are open to metallic inks, textures, etc. We would like to see options on both light and dark backgrounds. The font in the logo is Euro Technic Extended Regular.

```html
<!DOCTYPE html>
<html lang="en">
<head>
<meta charset="utf-8">
<title>Hollis Contracting – Business Card</title>
<link rel="stylesheet" href="https://fonts.googleapis.com/css2?family=Archivo:wght@400;600;800&display=swap">
<style>
  :root{
    --stage:#26272c;
    --card:#ffffff;
    --brand-blue:#1f4fb0;
    --panel-top:#1f74c6;
    --panel-bottom:#2a3c98;
    --silver:#8e9097;
    --ink-light:#ffffff;
  }
  *{margin:0;padding:0;box-sizing:border-box}
  html,body{width:1200px;height:800px;overflow:hidden;background:var(--stage);font-family:"Archivo",Arial,sans-serif}
  .stage{position:relative;width:1200px;height:800px;display:flex;align-items:center;justify-content:center;gap:40px}
  .card{position:relative;width:540px;height:310px;background:var(--card);border-radius:22px;overflow:hidden;box-shadow:0 18px 40px rgba(0,0,0,.45)}
  .wordmark{position:absolute;display:flex;align-items:center;gap:10px;color:var(--brand-blue);font-weight:800;line-height:1}
  .wordmark .mark-square{width:16px;height:16px;background:var(--brand-blue)}
  .wordmark .name{display:flex;flex-direction:column;gap:6px}
  .wordmark .name-main{font-size:46px;letter-spacing:3px}
  .wordmark .name-sub{font-size:13px;letter-spacing:2.4px}
  .card-front .wordmark{left:50%;top:50%;transform:translate(-50%,-50%)}
  .card-back .wordmark{left:34px;top:50%;transform:translateY(-50%)}
  .card-back .wordmark .name-main{font-size:36px}
  .card-back .wordmark .name-sub{font-size:10px;letter-spacing:1.8px}
  .panel{position:absolute;inset:0}
  .details{position:absolute;left:318px;top:34px;right:18px;color:var(--ink-light)}
  .holder-name{font-size:20px;font-weight:800;letter-spacing:.5px;text-transform:uppercase}
  .holder-title{font-size:14px;font-weight:400;margin-top:2px}
  .address{font-size:11.5px;line-height:1.35;margin-top:14px}
  .contacts{list-style:none;margin-top:12px}
  .contacts li{display:flex;align-items:center;gap:7px;font-size:11.5px;margin-bottom:6px}
  .contacts svg{flex:none;width:16px;height:16px}
  .motto{font-size:12px;font-weight:800;line-height:1.35;margin-top:10px}
</style>
</head>
<body>
<main class="stage">
  <section class="card card-front" aria-label="Card front">
    <div class="wordmark">
      <span class="mark-square"></span>
      <span class="name"><span class="name-main">HOLLIS</span><span class="name-sub">CONTRACTING, INC.</span></span>
    </div>
  </section>

  <section class="card card-back" aria-label="Card back">
    <svg class="panel" viewBox="0 0 540 310" width="540" height="310" aria-hidden="true">
      <defs>
        <linearGradient id="panelGradient" x1="0" y1="0" x2="1" y2="1">
          <stop offset="0" stop-color="var(--panel-top)"/>
          <stop offset="1" stop-color="var(--panel-bottom)"/>
        </linearGradient>
      </defs>
      <path d="M200 0 H540 V310 H300 C318 190 300 70 200 0 Z" fill="url(#panelGradient)"/>
      <path d="M214 4 C300 70 318 190 301 310" fill="none" stroke="var(--silver)" stroke-width="9"/>
    </svg>
    <div class="wordmark">
      <span class="mark-square"></span>
      <span class="name"><span class="name-main">HOLLIS</span><span class="name-sub">CONTRACTING, INC.</span></span>
    </div>
    <div class="details">
      <p class="holder-name">Dana Marlow</p>
      <p class="holder-title">Founder</p>
      <p class="address">PO BOX 480 Harbour Lane<br>2nd street Kestrel Bay</p>
      <ul class="contacts">
        <li><svg viewBox="0 0 16 16"><circle cx="8" cy="8" r="7.5" fill="#fff"/><path d="M5.2 4.2h1.6l.7 2-1 .8a5 5 0 0 0 2.5 2.5l.8-1 2 .7v1.6c0 .5-.4.9-.9.9A7 7 0 0 1 4.3 5.1c0-.5.4-.9.9-.9z" fill="var(--brand-blue)"/></svg>555 014 2876</li>
        <li><svg viewBox="0 0 16 16"><circle cx="8" cy="8" r="7.5" fill="#fff"/><rect x="4" y="5.2" width="8" height="5.6" rx=".6" fill="none" stroke="var(--brand-blue)" stroke-width="1.1"/><path d="M4.2 5.6 8 8.4l3.8-2.8" fill="none" stroke="var(--brand-blue)" stroke-width="1.1"/></svg>info@hollisbuild.com</li>
        <li><svg viewBox="0 0 16 16"><circle cx="8" cy="8" r="7.5" fill="#fff"/><g fill="none" stroke="var(--brand-blue)" stroke-width="1"><circle cx="8" cy="8" r="4"/><ellipse cx="8" cy="8" rx="1.8" ry="4"/><path d="M4 8h8"/></g></svg>www.hollisbuild.com</li>
      </ul>
      <p class="motto">Built on trust...<br>Driven by craftsmanship.</p>
    </div>
  </section>
</main>
</body>
</html>
```